Kid's Cancer Camp Business Card

Create a unique Two-Sided color business cards for Camp Willow Brook, a pediatric cancer camp.

The camp tag line is: A place where kids with cancer have fun...

Dale Morrisey, Executive Director
Camp Willow Brook Charitable Foundation, Inc
PO Box 918
Alder Falls, VT 06832

Phone - 203-555-0143
Fax - 203-555-0187
Email: dale@campwillowbrook.example
www.campwillowbrook.example

Target Market(s)

Potential Donors, Volunteers and Campers

Industry/Entity Type

Non-profit pediatric cancer camp

Contact Information for Business Card

All contact info that is included in the description

Font styles to use
Other font styles liked:
• Designer chooses font

Requirements
Must have
• Camp Willow Brook Logo and Tag Line
Nice to have
• should be eye catching
Should not have
• not cartoony

```html
<!DOCTYPE html>
<html lang="en">
<head>
<meta charset="utf-8">
<title>Camp Willow Brook – Business Card</title>
<link href="https://fonts.googleapis.com/css2?family=Lora:ital,wght@0,500;1,400&family=Montserrat:wght@400;800&display=swap" rel="stylesheet">
<style>
  :root {
    --card-blue: #0070a4;
    --sun-yellow: #fbb226;
    --white: #ffffff;
    --backdrop: #2a2b2d;
  }
  * { box-sizing: border-box; margin: 0; padding: 0; }
  html, body { width: 1200px; height: 1200px; overflow: hidden; }
  body {
    background: var(--backdrop);
    display: flex;
    align-items: center;
    justify-content: center;
    gap: 80px;
  }
  .card {
    width: 440px;
    height: 770px;
    background: var(--card-blue);
    border-radius: 32px;
    position: relative;
    display: flex;
    flex-direction: column;
    align-items: center;
    color: var(--white);
    text-align: center;
  }
  .brand {
    display: flex;
    flex-direction: column;
    align-items: center;
    gap: 22px;
  }
  .brand-dot {
    width: 54px; height: 54px;
    border-radius: 50%;
    background: var(--sun-yellow);
  }
  .brand-name {
    font-family: "Lora", serif;
    font-weight: 500;
    font-size: 44px;
    line-height: 1.05;
    color: var(--white);
    letter-spacing: 0.5px;
  }
  /* Front */
  .card-front .brand { margin-top: 230px; }
  .tagline {
    position: absolute;
    bottom: 90px;
    left: 0; right: 0;
    font-family: "Lora", serif;
    font-style: italic;
    font-size: 31px;
    line-height: 1.3;
    color: var(--sun-yellow);
  }
  /* Back */
  .card-back .brand { margin-top: 120px; }
  .holder-name {
    margin-top: 48px;
    font-family: "Montserrat", sans-serif;
    font-weight: 800;
    font-size: 29px;
    letter-spacing: 2px;
    color: var(--sun-yellow);
  }
  .holder-title {
    margin-top: 6px;
    font-family: "Montserrat", sans-serif;
    font-size: 19px;
    letter-spacing: 1px;
  }
  .icon-row {
    margin-top: 30px;
    display: flex;
    align-items: center;
    gap: 8px;
  }
  .icon-row .rule { width: 80px; height: 1px; background: var(--sun-yellow); margin: 0 10px; }
  .icon {
    width: 30px; height: 30px;
    border-radius: 6px;
    background: var(--sun-yellow);
    display: flex; align-items: center; justify-content: center;
  }
  .icon svg { width: 18px; height: 18px; }
  .contact-list {
    margin-top: 20px;
    list-style: none;
    font-family: "Montserrat", sans-serif;
    font-size: 17px;
    line-height: 1.5;
  }
  .divider { width: 320px; height: 1px; background: var(--sun-yellow); margin-top: 18px; }
  .org-address {
    margin-top: 16px;
    font-family: "Montserrat", sans-serif;
    font-size: 17px;
    line-height: 1.45;
    font-style: normal;
  }
</style>
</head>
<body>
  <section class="card card-front" aria-label="Card front">
    <div class="brand">
      <span class="brand-dot"></span>
      <span class="brand-name">camp willow brook</span>
    </div>
    <p class="tagline">A place where kids with<br>cancer have fun...</p>
  </section>

  <section class="card card-back" aria-label="Card back">
    <div class="brand">
      <span class="brand-dot"></span>
      <span class="brand-name">camp willow brook</span>
    </div>
    <h1 class="holder-name">DALE MORRISEY</h1>
    <p class="holder-title">Executive Director</p>

    <div class="icon-row">
      <span class="rule"></span>
      <span class="icon" aria-label="Phone">
        <svg viewBox="0 0 24 24"><path fill="#0070a4" d="M6.6 10.8a15 15 0 0 0 6.6 6.6l2.2-2.2c.3-.3.7-.4 1-.2 1.1.4 2.3.6 3.600.6.6 0 1 .4 1 1V20c0 .6-.4 1-1 1A17 17 0 0 1 3 4c0-.6.4-1 1-1h3.5c.6 0 1 .4 1 1 0 1.3.2 2.5.6 3.6.1.3 0 .7-.2 1z"/></svg>
      </span>
      <span class="icon" aria-label="Fax">
        <svg viewBox="0 0 24 24"><path fill="#0070a4" d="M7 3h10v4H7zM4 8h16a2 2 0 0 1 2 2v6h-4v5H6v-5H2v-6a2 2 0 0 1 2-2zm4 8v3h8v-3z"/></svg>
      </span>
      <span class="icon" aria-label="Email">
        <svg viewBox="0 0 24 24"><path fill="#0070a4" d="M3 5h18v14H3zm2 2v.5l7 4.5 7-4.5V7zm0 2.8V17h14V9.8l-7 4.5z"/></svg>
      </span>
      <span class="icon" aria-label="Website">
        <svg viewBox="0 0 24 24"><circle cx="12" cy="12" r="8.5" fill="none" stroke="#0070a4" stroke-width="2"/><path d="M3.5 12h17M12 3.5c3 3 3 14 0 17M12 3.5c-3 3-3 14 0 17" fill="none" stroke="#0070a4" stroke-width="1.6"/></svg>
      </span>
      <span class="rule"></span>
    </div>

    <ul class="contact-list">
      <li>203-555-0143</li>
      <li>203-555-0187</li>
      <li>dale@campwillowbrook.example</li>
      <li>www.campwillowbrook.example</li>
    </ul>
    <div class="divider"></div>
    <address class="org-address">
      Camp Willow Brook Charitable<br>
      Foundation, Inc<br>
      PO Box 918 Alder Falls, VT 06832
    </address>
  </section>
</body>
</html>
```